Thornwell Building Company - advertisement poster

I am looking to print some canvas signs to advertise my general contracting company, Thornwell Building Company. The sign will measure 6' long x 3' high so the size should match that ratio. I already have a logo icon, which is the Letter 'A' and some trees that I would like to incorporate, see attached. I would also like the to have the following information listed:
1) phone number: 472-318-6095
2) email: thornwellbuildingcompany@mailvistra.net
3) website: thornwellbuildingcompany.com
4) Lic#5386204
5) I want to use this text: "BUILD WITH THE T-CREW!"

The ad should be relatively simple and clean. Black and Green are my company colors. I am open to creative ideas!

Target Market(s)

People looking to renovate their homes

Industry/Entity Type

Construction

Colors
59FF00
82FF00
B8FF75
E3FFCB
F4FFEA

Requirements
Must have
• Must have my company logo
Should not have
• No photos or complex graphics

```html
<!DOCTYPE html>
<html lang="en">
<head>
<meta charset="UTF-8">
<title>Thornwell Building Company – Sign</title>
<link rel="stylesheet" href="https://fonts.googleapis.com/css2?family=Archivo+Black&family=Montserrat:wght@700;800&family=Roboto:wght@500&display=swap">
<style>
  :root {
    --ink: #000000;
    --paper: #ffffff;
    --green: #62a926;
    --canvas: #ffffff;
  }
  * { margin: 0; padding: 0; box-sizing: border-box; }
  html, body {
    width: 1200px; height: 1200px; overflow: hidden;
    background: var(--canvas);
  }
  .sign {
    position: absolute;
    left: 126px; top: 364px;
    width: 955px; height: 480px;
    background: var(--ink);
    overflow: hidden;
    box-shadow: 0 0 14px rgba(0,0,0,0.25);
  }
  .headline {
    position: absolute;
    left: 54px; top: 36px;
    font-family: 'Archivo Black', sans-serif;
    font-weight: 400;
    font-size: 106px;
    line-height: 93px;
    letter-spacing: -1px;
  }
  .headline-line {
    position: relative;
    display: block;
    white-space: nowrap;
  }
  .headline-line .fill { position: relative; z-index: 1; }
  .headline-line .outline {
    position: absolute; left: -5px; top: -4px; z-index: 2;
    color: transparent;
    -webkit-text-stroke: 1.3px var(--paper);
  }
  .headline-line.is-green .fill { color: var(--green); }
  .headline-line.is-white .fill { color: var(--paper); }
  .headline-line.is-white .outline { -webkit-text-stroke-color: var(--green); left: -8px; top: -3px; }

  .brand {
    position: absolute;
    left: 690px; top: 58px;
    width: 240px;
    display: flex; align-items: center; justify-content: center; gap: 12px;
    font-family: 'Montserrat', sans-serif;
    font-weight: 700;
    color: var(--paper);
    text-align: center;
  }
  .brand-square {
    width: 16px; height: 16px; background: var(--green); flex: none;
  }
  .brand-name { font-size: 20px; line-height: 24px; letter-spacing: 1px; }

  .phone-band {
    position: absolute; left: 487px; top: 355px;
    width: 468px; height: 60px;
    background: var(--paper);
    clip-path: polygon(14px 0, 100% 0, 100% 100%, 0 100%);
    z-index: 2;
  }
  .phone {
    position: absolute; left: 36px; top: 2px;
    font-family: 'Montserrat', sans-serif;
    font-weight: 800;
    font-size: 50px; line-height: 56px;
    letter-spacing: 4px;
    color: var(--green);
  }
  .contact-strip {
    position: absolute; left: 0; top: 412px;
    width: 955px; height: 43px;
    background: var(--green);
    display: flex; align-items: center; justify-content: space-between;
    padding: 0 44px 0 45px;
    font-family: 'Roboto', sans-serif;
    font-weight: 500;
    font-size: 19px;
    color: var(--paper);
  }
</style>
</head>
<body>
  <main class="sign">
    <h1 class="headline">
      <span class="headline-line is-green"><span class="fill">BUILD</span><span class="outline" aria-hidden="true">BUILD</span></span>
      <span class="headline-line is-white"><span class="fill">WITH THE</span><span class="outline" aria-hidden="true">WITH THE</span></span>
      <span class="headline-line is-green"><span class="fill">T-CREW!</span><span class="outline" aria-hidden="true">T-CREW!</span></span>
    </h1>

    <div class="brand">
      <span class="brand-square"></span>
      <span class="brand-name">THORNWELL<br>BUILDING COMPANY</span>
    </div>

    <div class="phone-band">
      <p class="phone">472-318-6095</p>
    </div>

    <footer class="contact-strip">
      <span class="email">thornwellbuildingcompany@mailvistra.net</span>
      <span class="website">thornwellbuildingcompany.com</span>
      <span class="license">Lic#5386204</span>
    </footer>
  </main>
</body>
</html>
```